ROBERTO VENTRANZI and his Orchestra "Under The Lanterns"

Music event. Friday November 6, 2015. Doors open 7pm
Venue - The Harwell Lane Hall, 47 Dunmore Rd. Perth. WA. 6000.
Roberto and his 12 piece band will perform inside a boxing ring in a very funky viby venue "The Harwell Lane Hall" in Perth, WA. The venue is a gorgeous retro looking place. See pics attached.
This "live music" event is focused on Roberto Ventranzi - with a twist. The 12 piece band and Roberto will be performing in the boxing ring - a really cool and quirky concept.
The whole event will be filmed and recorded - to make a DVD.
Updates

please don't focus on boxing this is a music event - the 11 piece band will perform in the boxing ring doesn't need to look "tough guy"

Target Market(s)

music lovers - 35 to 70. It needs to feel funky but still elegant focus to a mature fun loving audience "who have seen it all before".
Glitterati and Media event. Food lovers.....Tavolino Event Catering to provide italian tapas food included in the ticket price from 7pm to 8:30pm .....also includes 2 complimentary drinks

Industry/Entity Type

Gym

Font styles to use
Sans Serif

Requirements
Must have
• A powerful focus on Roberto Ventranzi and his band . . . and his music.
• A "wow factor" of it being "Under The Lanterns" a totally new concept in Perth nightlife entertainment. Basically, the boxing ring is the stage. ALSO, please mention that this event will be filmed with 8 cameras and digitally recorded. A 5.1 surround sound DVD will be made of this event . . . and we want "you" (the people) to be a part of it. And we'll have cameramen going through the crowd interviewing everyone for the "behind the scenes" section of the DVD. This is a super-exclusive event. Only 150 tix available - so get in quick.
Nice to have
• Included in the ticket price of $100 is 2 complimentary drinks (beer/wine/bubbly) and lots of delicious italian tapas food from 7pm to 8:30pm - provided by Tavolino Events Catering. Extra drinks including spirits and cocktails can be purchased at the bar. Show starts at 8:30pm sharp.
Should not have
• no typical Italian anything please

```html
<!DOCTYPE html>
<html lang="en">
<head>
<meta charset="utf-8">
<title>Roberto Ventranzi and His Orchestra — Under The Lanterns</title>
<link rel="stylesheet" href="https://fonts.googleapis.com/css2?family=Roboto:ital,wght@0,300;0,400;0,700;1,400;1,700&family=Roboto+Condensed:wght@700&display=swap">
<style>
  :root {
    --ink: #ffffff;
    --gold: #f2b51c;
    --gold-soft: rgba(238, 200, 120, 0.82);
    --dark: #2a2522;
    --bg-deep: #1c1412;
    --bg-warm: #6e3a2a;
    --bg-glow: #b0623a;
  }
  * { margin: 0; padding: 0; box-sizing: border-box; }
  html, body { width: 849px; height: 1200px; overflow: hidden; background: var(--bg-deep); }
  .poster {
    position: relative; width: 849px; height: 1200px; overflow: hidden;
    font-family: "Roboto", Arial, sans-serif; color: var(--ink);
  }
  .venue-photo {
    position: absolute; inset: 0;
    background:
      radial-gradient(ellipse at 30% 8%, rgba(210,120,80,0.55), transparent 45%),
      radial-gradient(ellipse at 20% 50%, rgba(150,70,40,0.5), transparent 50%),
      radial-gradient(ellipse at 80% 70%, rgba(110,55,35,0.45), transparent 55%),
      linear-gradient(180deg, var(--bg-warm) 0%, #4a2720 40%, #3a221d 70%, var(--bg-deep) 100%);
  }
  .headline { position: absolute; top: 22px; left: 0; right: 0; text-align: center; }
  .headline .artist { font-weight: 300; font-size: 50px; letter-spacing: 2px; line-height: 1.05; }
  .headline .orchestra { font-weight: 300; font-size: 50px; letter-spacing: 2px; line-height: 1.05; }
  .headline .show-title { margin-top: 14px; font-style: italic; font-size: 42px; letter-spacing: 1px; }
  .exclusive { position: absolute; top: 198px; left: 0; right: 0; text-align: center; font-size: 21px; letter-spacing: 0.5px; }
  .date-block { position: absolute; top: 262px; left: 236px; width: 380px; height: 260px; }
  .day-tab {
    position: absolute; left: 0; top: 0; width: 58px; height: 162px; background: var(--gold);
    display: flex; align-items: center; justify-content: center;
  }
  .day-tab span {
    transform: rotate(-90deg); font-family: "Roboto Condensed", Arial, sans-serif; font-weight: 700;
    font-size: 38px; color: var(--dark); letter-spacing: 1px; white-space: nowrap;
  }
  .month { position: absolute; left: 70px; top: -6px; font-family: "Roboto Condensed", Arial, sans-serif; font-weight: 700; font-size: 58px; color: var(--dark); letter-spacing: 1px; }
  .day-number { position: absolute; left: 66px; top: 30px; font-family: "Roboto Condensed", Arial, sans-serif; font-weight: 700; font-size: 250px; line-height: 1; color: var(--dark); letter-spacing: -4px; }
  .venue { position: absolute; top: 552px; left: 0; right: 0; text-align: center; font-size: 24px; }
  .venue .venue-name { color: var(--gold); font-style: italic; font-weight: 700; }
  .doors { position: absolute; top: 592px; left: 0; right: 0; text-align: center; }
  .doors .label { font-size: 26px; letter-spacing: 1px; }
  .doors .time { font-size: 64px; color: var(--gold); line-height: 1.05; }
  .recording { position: absolute; top: 718px; left: 0; right: 0; text-align: center; font-style: italic; font-size: 19px; line-height: 1.3; }
  .ticket-band {
    position: absolute; top: 772px; left: 0; width: 849px; height: 162px; background: var(--gold-soft);
    display: flex; align-items: center; padding: 0 28px 0 40px;
  }
  .caterer-mark {
    flex: none; width: 78px; height: 78px; background: var(--bg-deep);
    display: flex; align-items: center; justify-content: center;
    font-size: 13px; font-weight: 400; color: var(--ink); letter-spacing: 1px;
  }
  .ticket-details { flex: 1; text-align: center; color: var(--dark); font-size: 19px; line-height: 1.35; text-transform: uppercase; padding-left: 16px; }
</style>
</head>
<body>
<main class="poster">
  <div class="venue-photo" role="img" aria-label="Warm dimly lit retro hall with a boxing ring stage"></div>

  <header class="headline">
    <h1 class="artist">ROBERTO VENTRANZI</h1>
    <p class="orchestra">AND HIS ORCHESTRA</p>
    <p class="show-title">UNDER THE LANTERNS</p>
  </header>

  <p class="exclusive">THIS IS A SUPER-EXCLUSIVE EVENT &nbsp;- ONLY 150 TIX AVAILABLE -</p>

  <section class="date-block">
    <div class="day-tab"><span>FRIDAY</span></div>
    <div class="month">NOVEMBER</div>
    <div class="day-number">06</div>
  </section>

  <p class="venue"><span class="venue-name">THE HARWELL LANE HALL</span> -47 Dunmore Rd. Perth. WA. 6000</p>

  <div class="doors">
    <p class="label">DOORS OPEN</p>
    <p class="time">7:00PM</p>
  </div>

  <p class="recording">EVENT WILL BE FILMED WITH 8 CAMERAS AND DIGITALLY RECORDED IN 5.1 SURROUND SOUND</p>

  <section class="ticket-band">
    <div class="caterer-mark">TAVOLINO</div>
    <p class="ticket-details">Included in the ticket price of $100 is 2<br>complimentary drinks (beer/wine/bubbly)<br>and lots of delicious italian tapas<br>food from 7pm to 8:30pm - provided by<br>Tavolino Events Catering. Extra drinks including spirits<br>and cocktails can be purchased at the bar.</p>
  </section>
</main>
</body>
</html>
```